Harbor Lantern Note Card Stationary

We need a Note Card with envelope using the attached photo. I would like for photo
a. to bleed to the edges, no border or white space.
b. to have a weathered look if possible
c. to have two styles, folded and single.
d. to reflect the color of the photo as much as possible.
e. to provide following return address on envelope
Harbor Lantern 58 Tallowick Rd. Jamaica Plain MA 02187

Target Market(s)

Mailing List

Industry/Entity Type

Religious

Font styles to use
Other font styles liked:
• no preference

Requirements
Must have
• Varied sizes
Nice to have
• Weathers look
Should not have
• blurred finish, color distortion

```html
<!DOCTYPE html>
<html lang="en">
<head>
<meta charset="utf-8">
<title>Harbor Lantern Note Card</title>
<link rel="stylesheet" href="https://fonts.googleapis.com/css2?family=Jost:wght@400&family=Parisienne&display=swap">
<style>
  :root {
    --backdrop: #ecebe8;
    --envelope: #ffffff;
    --envelope-fold: #f1f1f1;
    --envelope-line: #dcdcdc;
    --address-gold: #b8955a;
    --title-ivory: #fbf7ee;
    --verse-cream: #f4e4a6;
    --sky-gold: #c8a774;
    --sky-dusk: #4e4050;
    --city-glow: #e9b868;
    --water-deep: #231c16;
  }
  html, body {
    margin: 0;
    padding: 0;
    width: 1200px;
    height: 848px;
    overflow: hidden;
    background: var(--backdrop);
  }
  .stage {
    position: relative;
    width: 1200px;
    height: 848px;
  }
  .envelope {
    position: absolute;
    left: 130px;
    top: 90px;
    width: 874px;
    height: 586px;
    background: var(--envelope);
    box-shadow: 0 1px 3px rgba(0,0,0,0.12);
  }
  .envelope-flap {
    position: absolute;
    left: 0;
    top: 0;
    width: 874px;
    height: 586px;
  }
  .return-address {
    position: absolute;
    left: 0;
    right: 0;
    top: 23px;
    margin: 0;
    text-align: center;
    font-family: "Jost", sans-serif;
    font-style: italic;
    font-size: 16px;
    letter-spacing: 0.2px;
    color: var(--address-gold);
  }
  .note-card {
    position: absolute;
    left: 214px;
    top: 176px;
    width: 868px;
    height: 585px;
    overflow: hidden;
    box-shadow: 0 2px 6px rgba(0,0,0,0.25);
  }
  .card-photo {
    position: absolute;
    inset: 0;
    background:
      linear-gradient(180deg,
        var(--sky-gold) 0%,
        #8f7657 22%,
        var(--sky-dusk) 44%,
        #5d4a45 52%,
        var(--city-glow) 66%,
        #6b4a2c 74%,
        var(--water-deep) 80%,
        #2b241d 100%);
  }
  .card-title {
    position: absolute;
    left: 0;
    right: 0;
    top: 72px;
    margin: 0;
    text-align: center;
    font-family: "Parisienne", cursive;
    font-weight: 400;
    font-size: 54px;
    color: var(--title-ivory);
  }
  .card-verse {
    position: absolute;
    left: 50px;
    right: 50px;
    top: 454px;
    margin: 0;
    text-align: center;
    font-family: "Jost", sans-serif;
    font-size: 17px;
    line-height: 21px;
    color: var(--verse-cream);
  }
</style>
</head>
<body>
  <main class="stage">
    <section class="envelope">
      <svg class="envelope-flap" viewBox="0 0 874 586" aria-hidden="true">
        <polygon points="0,0 874,0 874,40 850,106 40,106 0,40" fill="var(--envelope-fold)"/>
        <polyline points="0,0 40,106" fill="none" stroke="var(--envelope-line)" stroke-width="1"/>
        <polyline points="874,0 850,106" fill="none" stroke="var(--envelope-line)" stroke-width="1"/>
      </svg>
      <p class="return-address">Harbor Lantern 58 Tallowick Rd. Jamaica Plain MA 02187</p>
    </section>

    <article class="note-card">
      <div class="card-photo" role="img" aria-label="Night photograph of the Boston skyline lit up across dark harbor water under golden, streaked clouds"></div>
      <h1 class="card-title">In Boston as it is in Heaven</h1>
      <p class="card-verse">In all my prayers for all of you, i always pray with joy because of your partnership in the gospel from the first day until now...Philippians 1:4-5</p>
    </article>
  </main>
</body>
</html>
```